Floristry Business Card Design Project

I have a logo now and am looking to incorporate this into a business card. I would like a double sided business card. I would like one side to be decorative so that it blends well when included with floral arrangements and that can also be used as the front of a card and the other side will contain the business details. The font on the business details side should be clear although some decorative font would be ok. I have included the logo files for use in the business card design.

Feel free to break up the logo and use certain aspects of it in the design. Really looking for something that stands out and that is really creative.

Industry/Entity Type

Floral

Requirements
Should not have
• Nothing tacky or corny. The logo should be clearly read (perhaps a background colour).

```html
<!DOCTYPE html>
<html lang="en">
<head>
<meta charset="utf-8">
<title>Petal Hollow – Business Card</title>
<link rel="stylesheet" href="https://fonts.googleapis.com/css2?family=Cinzel:wght@400&family=Crimson+Text:wght@400;700&display=swap">
<style>
  :root {
    --page-bg: #e6e8e5;
    --card-bg: #fdfdfb;
    --brand-green: #5f9e7c;
    --band-green: #72b592;
    --band-line: #8cc4a6;
    --text-grey: #4f5552;
    --flora-coral: #e48b70;
    --flora-leaf: #9fc26b;
    --flora-teal: #6aae91;
    --card-shadow: rgba(40, 50, 45, 0.18);
  }
  * { box-sizing: border-box; margin: 0; padding: 0; }
  html, body {
    width: 1200px; height: 1000px; overflow: hidden;
    background: var(--page-bg);
  }
  .sheet {
    position: relative; width: 1200px; height: 1000px;
    display: flex; align-items: center; justify-content: center; gap: 40px;
  }
  .card {
    position: relative; width: 530px; height: 303px;
    background: var(--card-bg);
    box-shadow: 0 6px 18px var(--card-shadow);
    overflow: hidden;
  }
  /* Front */
  .card-front__frame {
    position: absolute; inset: 10px;
    border: 1px solid var(--brand-green);
  }
  .brand-mark {
    position: absolute; left: 50%; top: 34px; transform: translateX(-50%);
    width: 128px; height: 128px; border-radius: 50%;
    border: 2px solid var(--brand-green);
  }
  .brand-name {
    position: absolute; left: 0; right: 0; top: 182px;
    text-align: center;
    font-family: "Cinzel", serif; font-weight: 400;
    font-size: 24px; letter-spacing: 4px;
    color: var(--brand-green);
  }
  .flora-strip {
    position: absolute; left: 11px; right: 11px; bottom: 11px; height: 38px;
    background: linear-gradient(90deg, var(--flora-leaf), var(--flora-coral) 25%, var(--flora-teal) 50%, var(--flora-coral) 75%, var(--flora-leaf));
    opacity: 0.55;
  }
  /* Back */
  .card-back .rule {
    position: absolute; left: 0; right: 0; top: 58px; height: 2px;
    background: var(--band-line);
  }
  .card-back .band {
    position: absolute; left: 0; right: 0; top: 68px; height: 64px;
    background: var(--band-green);
  }
  .holder { position: absolute; left: 64px; top: 76px; color: #fff; font-family: "Crimson Text", serif; }
  .holder__name { font-weight: 700; font-size: 24px; line-height: 26px; }
  .holder__role { font-size: 16px; line-height: 20px; letter-spacing: 0.5px; }
  .contact {
    position: absolute; left: 64px; top: 150px;
    font-family: "Crimson Text", serif; font-size: 14px; line-height: 19px;
    color: var(--text-grey); letter-spacing: 0.4px;
  }
  .website {
    position: absolute; left: 64px; top: 224px;
    font-family: "Crimson Text", serif; font-size: 14px; letter-spacing: 1px;
    color: var(--text-grey);
  }
  .card-back .flora-strip { left: 0; right: 0; bottom: 0; height: 44px; }
</style>
</head>
<body>
  <main class="sheet">
    <section class="card card-front" aria-label="Card front">
      <div class="card-front__frame"></div>
      <div class="brand-mark"></div>
      <h1 class="brand-name">Petal Hollow</h1>
      <div class="flora-strip" role="img" aria-label="Border of small hand-drawn flowers and leaves"></div>
    </section>

    <section class="card card-back" aria-label="Card back">
      <div class="rule"></div>
      <div class="band"></div>
      <div class="holder">
        <p class="holder__name">Liam Carrow</p>
        <p class="holder__role">Managing Director</p>
      </div>
      <div class="contact">
        <p>001 555 01234</p>
        <p>liam@petalhollow.com</p>
      </div>
      <p class="website">www.PetalHollow.com</p>
      <div class="flora-strip" role="img" aria-label="Border of small hand-drawn flowers and leaves"></div>
    </section>
  </main>
</body>
</html>
```